<作成物>
■リッチメッセージ
リッチメニュー
合計2枚

【デザインの詳細】
デザインのイメージをファイルに入れております。
ロゴと・イメージのデザイン合わせた感じにしていただけると嬉しいです。
上下で一体感があるものを希望します。
https://22.datavault.test/0917-8a3c61f0b2d94e57c0a1d83e6b7f2c95

〈リッチメニューの表示項目〉
画像の中に入れますの、これを参考に入れてください。
この画像に似た物を作成してほしいというわけではありません。

デザイン重視でここの表示名はデザイン的に英語の方がよければ
英語でも大丈夫です。意味がわかって
ニュアンスがあっていれば文字を短くするのも
お任せします。あくまでデザイン重視です。
〈画像はこちらから〉

※こちらの作成以外に勝手に使用された場合は
著作権侵害で法的手段をとらせていただきます。
作成事例にもしようしないでください。

<サイズ>
・リッチメッセージ(1040×1040ピクセル)
・リッチメニュー(1200×810ピクセル)

<納品形式>
・ai形式(イラストレーターデータ)
・JPG
<詳細>
※添付ファイルをご確認ください。

<備考>
ブランディング効果を期待しています。
どんどん何個でも応募ください。

```html
<!DOCTYPE html>
<html lang="ja">
<head>
<meta charset="utf-8">
<title>メディケアビューティーMebuki. リッチメッセージ・リッチメニュー</title>
<link href="https://fonts.googleapis.com/css2?family=Noto+Serif+JP:wght@400;600;700;900&family=Noto+Sans+JP:wght@400;700&display=swap" rel="stylesheet">
<style>
:root{
  --pink:#e0407f;
  --pink-deep:#c8245f;
  --pink-soft:#f9dbe5;
  --red:#d4145a;
  --ink:#1f1a1c;
  --white:#ffffff;
  --tile-ink:#c72a63;
}
*{margin:0;padding:0;box-sizing:border-box}
html,body{width:766px;height:1200px;overflow:hidden;background:var(--white)}
body{font-family:"Noto Serif JP",serif;color:var(--ink);position:relative}

.message{position:absolute;left:0;top:0;width:766px;height:700px;
  background:linear-gradient(180deg,#fbe6ee 0%,#f7d3df 100%);overflow:hidden}
.message-band{position:absolute;top:0;left:0;width:100%;height:30px;background:var(--pink)}
.message-tag{position:absolute;top:6px;left:50%;transform:translateX(-50%);
  background:var(--white);color:var(--pink-deep);font-weight:700;font-size:18px;
  padding:1px 20px;border-radius:4px;letter-spacing:2px;white-space:nowrap}
.brand-mark{position:absolute;left:40px;top:44px;width:86px;height:86px;border-radius:50%;
  background:var(--white);display:flex;align-items:center;justify-content:center;
  color:var(--pink);font-weight:700;font-size:19px}
.title{position:absolute;top:46px;left:140px;right:20px;text-align:center;
  color:var(--pink);font-weight:900;font-size:33px;line-height:1.2;white-space:nowrap}
.title-open{display:block;font-size:52px;line-height:1.1;margin-right:120px}
.campaign{position:absolute;top:120px;right:40px;background:var(--pink);color:var(--white);
  font-size:15px;font-weight:600;padding:3px 10px}

.menu-panel{position:absolute;left:28px;top:182px;width:710px;height:470px;background:var(--white);
  display:flex;padding:20px 14px}
.menu-col{flex:1;padding:0 14px}
.menu-col + .menu-col{border-left:2px solid var(--pink-soft)}
.menu-heading{font-size:34px;font-weight:900;margin-bottom:8px;letter-spacing:1px}
.item{margin-bottom:18px}
.menu-col + .menu-col .item{margin-bottom:34px}
.item-name{color:var(--pink);font-size:22px;font-weight:700;line-height:1.3}
.item-name small{font-size:14px}
.item-note{font-size:14px;line-height:1.4}
.price-row{display:flex;align-items:center;gap:6px;margin-top:4px}
.time{background:var(--ink);color:var(--white);font-family:"Noto Sans JP",sans-serif;
  font-size:18px;font-weight:700;padding:2px 7px;line-height:1.2}
.price{color:var(--red);font-size:38px;font-weight:900;line-height:1}
.price small{font-size:24px}
.footnote{position:absolute;left:28px;right:28px;top:664px;font-size:13px;text-align:center;color:var(--ink)}

.rich-menu{position:absolute;left:0;top:725px;width:766px;height:475px;
  background:linear-gradient(180deg,#f8d6e1,#f3c2d3);
  display:grid;grid-template-columns:repeat(3,240px);grid-template-rows:repeat(2,214px);
  gap:15px 11px;padding:16px 12px}
.tile{background:var(--white);display:flex;flex-direction:column;align-items:center;justify-content:center;
  color:var(--tile-ink);text-align:center}
.tile.accent{background:var(--pink);color:var(--white)}
.tile svg{width:90px;height:90px;margin-bottom:10px}
.tile-label{font-size:28px;font-weight:700;letter-spacing:1px}
.shop-kicker{font-size:19px;font-weight:700;color:var(--ink);white-space:nowrap}
.shop-name{font-size:56px;font-weight:700;line-height:1.1;color:var(--ink)}
.shop-branch{margin-top:6px;background:var(--pink);color:var(--white);font-size:19px;padding:2px 14px}
</style>
</head>
<body>

<section class="message">
  <div class="message-band"></div>
  <div class="message-tag">桜川駅前HIFU 専門店</div>
  <div class="brand-mark">Mebuki</div>
  <h1 class="title">メディケアビューティーMebuki.<span class="title-open">OPEN!!</span></h1>
  <div class="campaign">8月・9月キャンペーン</div>

  <div class="menu-panel">
    <div class="menu-col">
      <div class="menu-heading">最新美肌光脱毛</div>
      <div class="item">
        <div class="item-name">レディース<small>（高校生より）</small></div>
        <div class="item-note">脇+腕毛（美肌パック付き）</div>
        <div class="price-row"><span class="time">40分</span><span class="price">5,000<small>円</small></span></div>
      </div>
      <div class="item">
        <div class="item-name">メンズ</div>
        <div class="item-note">ヒゲ脱毛+顔脱毛（おでこ、頬、鼻）</div>
        <div class="price-row"><span class="time">40分</span><span class="time">1部</span><span class="price">3,000<small>円〜</small></span></div>
      </div>
      <div class="item">
        <div class="item-name">キッズ<small>（10歳〜中学生）</small></div>
        <div class="item-note">脇+肘下脱毛1部位</div>
        <div class="price-row"><span class="time">20分</span><span class="price">1,200<small>円〜</small></span></div>
      </div>
    </div>
    <div class="menu-col">
      <div class="item">
        <div class="item-name">エイジングケアフェイシャル</div>
        <div class="item-note">通常8,000円のところ</div>
        <div class="price-row"><span class="time">60分</span><span class="price">6,000<small>円</small></span></div>
      </div>
      <div class="item">
        <div class="item-name">よもぎペア蒸し<small>（お二人様同室）</small></div>
        <div class="item-note">お一人様</div>
        <div class="price-row"><span class="time">45分</span><span class="price">3,000<small>円</small></span></div>
      </div>
      <div class="item">
        <div class="item-name">ボディケアケア</div>
        <div class="item-note">全身ボディケア×首こり撃退コース</div>
        <div class="price-row"><span class="time">90分</span><span class="price">5,200<small>円</small></span></div>
      </div>
    </div>
  </div>
  <p class="footnote">ラッシュリフト・まつ毛パーマ・フラットラッシュ・エクステ　アイリスト在籍サロン</p>
</section>

<nav class="rich-menu">
  <div class="tile">
    <div class="shop-kicker">セラピー&amp;スクール</div>
    <div class="shop-name">Mebuki</div>
    <div class="shop-branch">港町店</div>
  </div>
  <div class="tile accent">
    <svg viewBox="0 0 100 100"><rect x="8" y="12" width="84" height="62" rx="14" fill="#fff"/><path d="M30 72 L24 92 L48 72Z" fill="#fff"/><circle cx="32" cy="43" r="6" fill="#e0407f"/><circle cx="50" cy="43" r="6" fill="#e0407f"/><circle cx="68" cy="43" r="6" fill="#e0407f"/></svg>
    <div class="tile-label">SNS</div>
  </div>
  <div class="tile">
    <svg viewBox="0 0 100 100" fill="none" stroke="#c72a63" stroke-width="5"><rect x="14" y="14" width="60" height="76" rx="4"/><line x1="26" y1="8" x2="26" y2="20"/><line x1="44" y1="8" x2="44" y2="20"/><line x1="62" y1="8" x2="62" y2="20"/><line x1="24" y1="38" x2="60" y2="38"/><line x1="24" y1="52" x2="52" y2="52"/><line x1="24" y1="66" x2="46" y2="66"/><path d="M84 36 L60 78 L56 90 L66 82 L90 40Z"/></svg>
    <div class="tile-label">スクール情報</div>
  </div>
  <div class="tile">
    <div class="shop-kicker">メディケアビューティー</div>
    <div class="shop-name">Mebuki</div>
    <div class="shop-branch">桜川店</div>
  </div>
  <div class="tile">
    <svg viewBox="0 0 100 100" fill="#c72a63"><circle cx="30" cy="28" r="11"/><rect x="16" y="42" width="28" height="44" rx="8"/><circle cx="70" cy="28" r="11"/><rect x="56" y="42" width="28" height="44" rx="8"/><path d="M42 60 h16 l-4 -5 M58 60 l-4 5" stroke="#c72a63" stroke-width="4" fill="none"/></svg>
    <div class="tile-label">紹介する</div>
  </div>
  <div class="tile">
    <svg viewBox="0 0 100 100"><path d="M26 10 L40 10 L46 32 L36 40 C42 54 48 60 60 66 L68 56 L90 62 L90 76 C90 84 84 90 76 90 C40 88 12 60 10 24 C10 16 16 10 26 10Z" fill="#c72a63"/></svg>
    <div class="tile-label">電話予約</div>
  </div>
</nav>

</body>
</html>
```